Business Card Design

I am an Event and Wedding Planner in need of an eye catching business card featuring my logo (attached), my contact details, and my company tagline (Making each one of your gatherings radiant...) I would like the tagline in font similar the logo's font.
Updates
I have just noticed that my logo has a misspelling so for the final design, I will be uploading a corrected logo as soon as I have it.
My apologies.
Reason: Waiting on a corrected logo...Occasions is misspelled and it should say Weddings not Wedding
The logo has been corrected so now Occasions is spelled correctly and it says Weddings instead of Wedding. Please use Edwardian Script ITC as the font for the tagline so it will match the logo. Thank you for your patience.
Target Market(s)
Engaged couples and people hosting milestone celebrations. 25-50 years old, predominately female
Industry/Entity Type
Business
Contact Information for Business Card
Delphine Marsh, Event Manager / Owner, Mobile: 0491 836 254, Email: delphine@radiantgatheringsco.com.au, www.radiantgatheringsco.com.au, Making each one of your gatherings radiant...

```html
<!DOCTYPE html>
<html lang="en">
<head>
<meta charset="utf-8">
<title>Radiant Gatherings Co — Business Card</title>
<link rel="stylesheet" href="https://fonts.googleapis.com/css2?family=Exo+2:wght@400;500;600&family=Pinyon+Script&display=swap">
<style>
  :root {
    --bg: #e6e4e1;
    --card: #ffffff;
    --ink: #111111;
    --text: #2a2a2a;
    --red: #c8333a;
    --grey: #9a9a9a;
  }
  * { margin: 0; padding: 0; box-sizing: border-box; }
  html, body { width: 1200px; height: 900px; overflow: hidden; background: var(--bg); }
  .canvas { position: relative; width: 1200px; height: 900px; display: flex; align-items: center; justify-content: center; }
  .card {
    position: relative; width: 1000px; height: 572px; background: var(--card);
    border-radius: 48px; overflow: hidden; box-shadow: 0 14px 40px rgba(0,0,0,.18);
    font-family: "Exo 2", sans-serif; color: var(--text);
  }
  .card__swoosh { position: absolute; inset: 0; width: 100%; height: 100%; }
  .brand { position: absolute; left: 60px; top: 132px; display: flex; align-items: center; gap: 14px; }
  .brand__name { font-size: 38px; font-weight: 500; color: var(--ink); letter-spacing: .5px; }
  .brand__dot { width: 14px; height: 14px; border-radius: 50%; background: var(--red); }
  .brand__rule { position: absolute; left: 60px; top: 200px; width: 390px; height: 1.5px; background: var(--grey); }
  .tagline { position: absolute; left: 62px; top: 208px; font-family: "Pinyon Script", cursive; font-size: 28px; color: var(--ink); white-space: nowrap; }
  .address { position: absolute; left: 60px; top: 292px; font-size: 21px; font-weight: 500; line-height: 1.5; letter-spacing: 1px; color: var(--text); }
  .person { position: absolute; right: 80px; top: 52px; text-align: right; }
  .person__name { font-size: 23px; font-weight: 600; letter-spacing: 2px; text-transform: uppercase; color: var(--ink); }
  .person__title { font-size: 14px; font-weight: 500; letter-spacing: 2.5px; text-transform: uppercase; color: var(--text); margin-top: 2px; }
  .contacts { position: absolute; right: 80px; top: 126px; list-style: none; text-align: right; }
  .contacts__item { display: flex; justify-content: flex-end; align-items: center; gap: 12px; font-size: 15px; letter-spacing: 1.2px; line-height: 28px; color: var(--text); white-space: nowrap; }
  .contacts__icon { flex: 0 0 17px; width: 17px; height: 17px; fill: none; stroke: var(--red); stroke-width: 2; }
  .contacts__icon--solid { fill: var(--red); stroke: none; }
  .contacts__icon--mail { fill: var(--red); stroke: var(--card); stroke-width: 1.4; }
</style>
</head>
<body>
<main class="canvas">
  <section class="card" aria-label="Radiant Gatherings Co business card">
    <svg class="card__swoosh" viewBox="0 0 1000 572" preserveAspectRatio="none" aria-hidden="true">
      <path fill="var(--ink)" d="M0 462 C320 462 720 430 1000 338 L1000 572 L0 572 Z"/>
      <path fill="var(--red)" d="M270 448 C600 432 860 378 1000 288 L1000 322 C860 404 600 442 270 448 Z"/>
    </svg>

    <div class="brand">
      <span class="brand__name">Radiant Gatherings Co</span>
      <span class="brand__dot"></span>
    </div>
    <div class="brand__rule"></div>
    <p class="tagline">Making each one of your gatherings radiant...</p>

    <p class="address">Level 3, 12 Harbour Lane<br>Sydney</p>

    <div class="person">
      <p class="person__name">Delphine Marsh</p>
      <p class="person__title">Event Manager / Owner</p>
    </div>

    <ul class="contacts">
      <li class="contacts__item">02 9384 1170
        <svg class="contacts__icon" viewBox="0 0 20 20"><path d="M4 2 L8 2 L9 6 L7 8 C8 11 9 12 12 13 L14 11 L18 12 L18 16 C18 17 17 18 16 18 C8 18 2 12 2 4 C2 3 3 2 4 2 Z"/></svg>
      </li>
      <li class="contacts__item">0491 836 254
        <svg class="contacts__icon" viewBox="0 0 20 20"><rect x="5" y="1.5" width="10" height="17" rx="2"/><line x1="9" y1="15.5" x2="11" y2="15.5"/></svg>
      </li>
      <li class="contacts__item">02 9384 1171
        <svg class="contacts__icon contacts__icon--solid" viewBox="0 0 20 20"><rect x="6" y="2" width="8" height="5"/><rect x="2" y="8" width="16" height="10" rx="1.5"/></svg>
      </li>
      <li class="contacts__item">delphine@radiantgatheringsco.com.au
        <svg class="contacts__icon contacts__icon--mail" viewBox="0 0 20 20"><rect x="1.5" y="4" width="17" height="12" rx="1"/><path d="M2 4.5 L10 11 L18 4.5" fill="none"/></svg>
      </li>
      <li class="contacts__item">www.radiantgatheringsco.com.au
        <svg class="contacts__icon" viewBox="0 0 20 20"><circle cx="10" cy="10" r="8"/><ellipse cx="10" cy="10" rx="3.5" ry="8"/><line x1="2" y1="10" x2="18" y2="10"/></svg>
      </li>
    </ul>
  </section>
</main>
</body>
</html>
```